Referral Flyer Marketing Flyer 8.5" x 5.5" (Half Page) Front & Back

Designer Instructions – Updated Referral Program Flyer

(Based on the mock-up in “Brief Layout and Instructions.pdf”)

OVERALL STYLE + LAYOUT

Maintain the same general layout, structure, and flow as the mock-up flyer (front and back).

This is an update of an older flyer, not a full redesign — keep the same sections, proportions, and overall visual feel, but with cleaner, more modern design improvements.

The final flyer should look clean, bold, professional, and high-impact, geared toward realtors, property managers, and contractors who refer work.

FRONT SIDE INSTRUCTIONS
1. Header Section

Remove the Tidewell Renovation logo from the top banner.
(Shown on page 1 of the PDF)

2. Main Headline

Keep the same three-line structure:
EARN
UNLIMITED
CASH

Center it, maximize impact, and increase the font size of CASH so all three words match in importance.

Make the headline bold, clean, and the main focal point.

3. Cash Incentive Box

Keep the "$500 minimum OR 10% per referral" box, but upgrade the graphics to look sharper and more modern.

Ensure the wording matches exactly what’s in the mock-up.

4. Premier Partner Program Ribbon

Clean up and modernize the "PREMIER PARTNER PROGRAM" bar while keeping the same position and structure.

Ensure the checkmark badge remains crisp and professional.

5. Supporting Icons Section

Keep the four icons/benefit boxes (Guaranteed Payout, Free Evaluations, Affordable Solutions, Industry Leaders) in the same order.

Update the icons to cleaner, more modern styles — but maintain the same meanings.

Improve alignment and spacing for sharper visual consistency.

6. Remove Icons in Contact Area

At the bottom (“CALL TEXT OR BOOK ONLINE 858-472-6190 BrightKeelRebuilds.com”), remove the phone and internet icons, as noted on page 2 of the PDF.

7. Replace All Images

I (Dorian) will provide all updated stock images separately via email.

Replace the flood/water-damage imagery and roof leak with the new images I send.

Keep image placement and proportions the same as the mock-up.

BACK SIDE INSTRUCTIONS
1. Header Image + “REFER / EARN” Section

Maintain the same large split-image layout (“The more you refer, the more you earn”).

Replace all background imagery with the new assets I will send.

Keep the CASH FLOW image section but modernize the type and spacing.

2. “HOW IT WORKS” Section

Preserve the three-column layout:

Refer Flood, Water & Mold Damage

We Take Care of Everything (evaluations/insurance)

Get Paid to Share

Update images, tighten spacing, and use modern iconography.

3. Remove Phone/Internet Icons

Same as the front side — remove small communication icons and keep only the text/number/URL.

4. Bottom Contact Bar

Keep the blue bar, same wording, same layout — just modernize the style if needed for clarity.

5. Replace All Back-Side Images

Again, I will email you the image assets.

Keep the layout EXACT — just update with higher-quality photos and improved design.

TEXT CONTENT (Keep as-is unless spacing adjustments needed)

All text shown in the PDF should remain exactly the same unless spacing or visual balance requires minor adjustments.
Example from page 3:

“REFER FLOOD, MOLD & CONSTRUCTION JOBS”

“We Schedule a Free Estimate. If Approved, You Get Paid.”

“Everybody Benefits From Referrals”

Everything stays, just refreshed and visually improved.

DESIGN GOALS

Flyer should look high-end and trustworthy, not salesy.

Consistent color theme: blues, whites, yellows, same palette as original.

Use bold, modern fonts with strong readability.

Ensure all headlines pop and all benefit boxes are clean, well-aligned, and evenly spaced.

The final result should feel like a premium referral program flyer for a top-tier restoration/remodel company.

FILES I WILL PROVIDE

I will send the designer:

All replacement stock photos

Any updated logos (if needed)

Original high-resolution version of the mock-up (if available)

Any additional icons preferred

Colors
0054AA
0677BA
7BADD7
CADEEF
E8F1F8

Requirements
Must have
• Designer Instructions – Updated Referral Program Flyer (Based on the mock-up in “Brief Layout and Instructions.pdf”) OVERALL STYLE + LAYOUT Maintain the same general layout, structure, and flow as the mock-up flyer (front and back). This is an update of an older flyer, not a full redesign — keep the same sections, proportions, and overall visual feel, but with cleaner, more modern design improvements. The final flyer should look clean, bold, professional, and high-impact, geared toward realtors, property managers, and contractors who refer work. FRONT SIDE INSTRUCTIONS 1. Header Section Remove the Tidewell Renovation logo from the top banner. (Shown on page 1 of the PDF) 2. Main Headline Keep the same three-line structure: EARN UNLIMITED CASH Center it, maximize impact, and increase the font size of CASH so all three words match in importance. Make the headline bold, clean, and the main focal point. 3. Cash Incentive Box Keep the "$500 minimum OR 10% per referral" box, but upgrade the graphics to look sharper and more modern. Ensure the wording matches exactly what’s in the mock-up. 4. Premier Partner Program Ribbon Clean up and modernize the "PREMIER PARTNER PROGRAM" bar while keeping the same position and structure. Ensure the checkmark badge remains crisp and professional. 5. Supporting Icons Section Keep the four icons/benefit boxes (Guaranteed Payout, Free Evaluations, Affordable Solutions, Industry Leaders) in the same order. Update the icons to cleaner, more modern styles — but maintain the same meanings. Improve alignment and spacing for sharper visual consistency. 6. Remove Icons in Contact Area At the bottom (“CALL TEXT OR BOOK ONLINE 858-472-6190 BrightKeelRebuilds.com”), remove the phone and internet icons, as noted on page 2 of the PDF. 7. Replace All Images I (Dorian) will provide all updated stock images separately via email. Replace the flood/water-damage imagery and roof leak with the new images I send. Keep image placement and proportions the same as the mock-up. BACK SIDE INSTRUCTIONS 1. Header Image + “REFER / EARN” Section Maintain the same large split-image layout (“The more you refer, the more you earn”). Replace all background imagery with the new assets I will send. Keep the CASH FLOW image section but modernize the type and spacing. 2. “HOW IT WORKS” Section Preserve the three-column layout: Refer Flood, Water & Mold Damage We Take Care of Everything (evaluations/insurance) Get Paid to Share Update images, tighten spacing, and use modern iconography. 3. Remove Phone/Internet Icons Same as the front side — remove small communication icons and keep only the text/number/URL. 4. Bottom Contact Bar Keep the blue bar, same wording, same layout — just modernize the style if needed for clarity. 5. Replace All Back-Side Images Again, I will email you the image assets. Keep the layout EXACT — just update with higher-quality photos and improved design. TEXT CONTENT (Keep as-is unless spacing adjustments needed) All text shown in the PDF should remain exactly the same unless spacing or visual balance requires minor adjustments. Example from page 3: “REFER FLOOD, MOLD & CONSTRUCTION JOBS” “We Schedule a Free Estimate. If Approved, You Get Paid.” “Everybody Benefits From Referrals” Everything stays, just refreshed and visually improved. DESIGN GOALS Flyer should look high-end and trustworthy, not salesy. Consistent color theme: blues, whites, yellows, same palette as original. Use bold, modern fonts with strong readability. Ensure all headlines pop and all benefit boxes are clean, well-aligned, and evenly spaced. The final result should feel like a premium referral program flyer for a top-tier restoration/remodel company. FILES I WILL PROVIDE I will send the designer: All replacement stock photos Any updated logos (if needed) Original high-resolution version of the mock-up (if available) Any additional icons preferred

```html
<!DOCTYPE html>
<html lang="en">
<head>
<meta charset="utf-8">
<title>Referral Program Flyer – Front &amp; Back</title>
<link href="https://fonts.googleapis.com/css2?family=Montserrat:wght@500;700;800;900&family=Oswald:wght@600;700&display=swap" rel="stylesheet">
<style>
  :root{
    --page:#e6e6e6;
    --navy:#1f3270;
    --navy-deep:#14204d;
    --royal:#1e4896;
    --ink:#0f1a38;
    --yellow:#f7df1e;
    --orange:#f7941d;
    --red:#c6202b;
    --white:#ffffff;
    --photo-room:#9aa3ab;
    --photo-cash:#c9cfc5;
  }
  *{box-sizing:border-box;margin:0;padding:0}
  html,body{width:1200px;height:1200px;overflow:hidden;background:var(--page)}
  body{position:relative;font-family:"Montserrat",Arial,sans-serif;color:var(--navy)}

  .flyer{position:absolute;left:198px;width:1004px;height:649px;background:var(--white);
    transform:scale(.8);transform-origin:0 0;overflow:hidden}
  .flyer--front{top:66px}
  .flyer--back{top:618px}

  /* shared contact bar */
  .contact-bar{position:absolute;left:0;right:0;bottom:0;height:59px;display:flex;align-items:center}
  .contact-bar__label{position:absolute;left:0;top:0;height:59px;width:420px;background:var(--navy);
    clip-path:polygon(0 0,370px 0,420px 100%,0 100%);color:var(--white);font-weight:800;font-size:19px;
    display:flex;align-items:center;padding-left:48px}
  .contact-bar__details{position:absolute;left:436px;right:0;top:0;height:59px;display:flex;align-items:center;gap:14px;color:var(--navy)}
  .contact-bar__phone{font-weight:800;font-size:27px}
  .contact-bar__sep{width:3px;height:28px;background:var(--navy)}
  .contact-bar__web{font-weight:700;font-size:19px}

  /* FRONT */
  .front-hero{position:absolute;left:0;top:0;width:600px;height:307px;
    background:linear-gradient(180deg,#1f3270 0%,#233a7c 100%)}
  .front-hero__skyline{position:absolute;left:0;bottom:0;width:600px;height:180px;
    background:linear-gradient(180deg,rgba(30,50,100,0) 0%,#1a2a5c 60%,#13204a 100%)}
  .front-headline{position:absolute;left:0;top:30px;width:530px;text-align:center;font-weight:900;line-height:.9}
  .front-headline__earn{display:block;color:var(--yellow);font-size:92px;letter-spacing:1px}
  .front-headline__unlimited{display:block;color:var(--white);font-size:64px;margin-top:4px}
  .front-headline__cash{display:block;color:var(--yellow);font-size:92px;margin-top:4px}
  .front-photo{position:absolute;top:0;right:0;width:475px;height:307px;
    background:linear-gradient(160deg,#c9c9c4 0%,var(--photo-room) 50%,#4b91b8 100%);
    clip-path:polygon(56px 0,100% 0,100% 100%,56px 100%,0 52%)}
  .refer-band{position:absolute;left:0;top:265px;width:585px;height:42px;background:var(--yellow);
    clip-path:polygon(0 0,100% 0,calc(100% - 20px) 100%,0 100%);
    display:flex;align-items:center;padding-left:73px;font-weight:800;font-size:27px;color:var(--navy)}
  .offer-band{position:absolute;left:0;top:307px;width:585px;height:83px;background:var(--red);
    clip-path:polygon(0 0,100% 0,calc(100% - 45px) 100%,0 100%);color:var(--white)}
  .offer-band__amount{position:absolute;left:56px;top:6px;font-weight:900;font-size:46px;line-height:1}
  .offer-band__minimum{position:absolute;left:70px;top:53px;font-weight:800;font-size:17px}
  .offer-band__slash{position:absolute;left:196px;top:0;width:60px;height:83px}
  .offer-band__or{position:absolute;left:207px;top:26px;width:34px;height:34px;border-radius:50%;background:var(--white);
    color:var(--red);font-weight:900;font-size:15px;display:flex;align-items:center;justify-content:center}
  .offer-band__percent{position:absolute;left:266px;top:8px;font-weight:900;font-size:58px;line-height:1}
  .offer-band__percent-sign{position:absolute;left:338px;top:12px;width:26px;height:26px;border:2px solid var(--white);border-radius:50%;
    font-size:15px;font-weight:800;display:flex;align-items:center;justify-content:center}
  .offer-band__per{position:absolute;left:372px;top:16px;font-weight:800;font-size:23px;line-height:1.1}
  .partner-ribbon{position:absolute;left:592px;top:325px;width:365px;height:64px;background:var(--red);
    border-radius:32px 0 0 32px}
  .partner-ribbon__text{position:absolute;left:0;width:295px;text-align:center;color:var(--white);line-height:1}
  .partner-ribbon__premier{top:8px;font-weight:500;font-size:22px;letter-spacing:5px}
  .partner-ribbon__program{top:33px;font-weight:800;font-size:24px}
  .partner-ribbon__badge{position:absolute;right:10px;top:5px;width:54px;height:56px}
  .wins{position:absolute;left:0;right:0;top:402px;text-align:center;font-weight:800;font-size:22px;color:var(--navy)}
  .benefits{position:absolute;left:88px;top:438px;display:flex;gap:23px}
  .benefit{position:relative;width:190px;height:97px;border:3px solid var(--navy);border-radius:16px}
  .benefit__title{height:46px;display:flex;align-items:center;justify-content:center;text-align:center;
    font-weight:800;font-size:14px;line-height:1.1;color:var(--navy);border-bottom:3px solid var(--navy);
    border-radius:0 0 14px 14px;margin:0 6px}
  .benefit__body{display:flex;align-items:center;gap:8px;padding:4px 8px 0 14px}
  .benefit__icon{flex:0 0 30px;width:30px;height:30px}
  .benefit__text{font-size:9.5px;font-weight:700;line-height:1.25;color:var(--navy)}
  .benefit__dot{position:absolute;right:-4px;bottom:-4px;width:9px;height:9px;border-radius:50%;background:var(--navy)}
  .tagline{position:absolute;left:0;right:0;top:548px;text-align:center;font-weight:900;font-size:27px;color:var(--navy)}
  .tagline em{font-style:normal;color:var(--red)}

  /* BACK */
  .back-hero{position:absolute;left:0;top:0;width:600px;height:307px;background:var(--royal)}
  .back-hero__shade{position:absolute;left:0;top:0;width:600px;height:307px;background:var(--ink);
    clip-path:polygon(120px 40px,300px 40px,600px 307px,120px 307px)}
  .back-photo{position:absolute;top:0;right:0;width:555px;height:307px;
    background:linear-gradient(135deg,#d8dbd2 0%,var(--photo-cash) 45%,#b6bfb2 100%);
    clip-path:polygon(0 0,100% 0,100% 100%,130px 100%)}
  .back-headline{position:absolute;left:120px;top:36px;font-family:"Oswald",Arial,sans-serif;font-weight:700;
    white-space:nowrap;text-align:left}
  .back-headline__lead{display:block;color:var(--white);font-size:35px;line-height:40px;letter-spacing:-.3px}
  .back-headline__big{display:block;font-size:92px;line-height:88px;letter-spacing:-1px;
    background:linear-gradient(180deg,var(--yellow) 0%,var(--orange) 100%);-webkit-background-clip:text;background-clip:text;color:transparent}
  .how-band{position:absolute;left:0;top:307px;width:418px;height:48px;background:var(--yellow);
    clip-path:polygon(0 0,100% 0,calc(100% - 45px) 100%,0 100%);display:flex;align-items:center;padding-left:48px;
    font-weight:800;font-size:27px;color:var(--navy)}
  .steps{position:absolute;left:88px;top:378px;display:flex;gap:21px}
  .step{width:262px;height:192px;border:2px solid var(--navy);border-radius:12px;overflow:hidden;display:flex;flex-direction:column}
  .step__photo{height:118px}
  .step__photo--scan{background:linear-gradient(90deg,#e8e2d6 0%,#cfae80 55%,#c9386a 75%,#3a3a3a 100%)}
  .step__photo--inspect{background:linear-gradient(180deg,#c7d3de 0%,#8fa39a 60%,#5f7a9b 100%)}
  .step__photo--sign{background:linear-gradient(180deg,#5f9fd8 0%,#c5dcef 60%,#8db8e0 100%)}
  .step__label{flex:1;display:flex;flex-direction:column;align-items:center;justify-content:center;text-align:center;
    font-weight:800;font-size:18px;line-height:1.15;color:var(--navy)}
  .step__note{font-weight:500;font-size:14px;margin-top:2px}
</style>
</head>
<body>

<section class="flyer flyer--front" aria-label="Referral flyer front">
  <div class="front-hero">
    <div class="front-hero__skyline" role="img" aria-label="Night city skyline silhouette"></div>
    <h1 class="front-headline">
      <span class="front-headline__earn">EARN</span>
      <span class="front-headline__unlimited">UNLIMITED</span>
      <span class="front-headline__cash">CASH</span>
    </h1>
  </div>
  <div class="front-photo" role="img" aria-label="Blue air movers and dehumidifiers drying a flooded basement room"></div>

  <div class="refer-band">GET PAID TO REFER A FLOOD</div>
  <div class="offer-band">
    <span class="offer-band__amount">$500</span>
    <span class="offer-band__minimum">MINIMUM</span>
    <svg class="offer-band__slash" viewBox="0 0 60 83"><line x1="55" y1="5" x2="5" y2="78" stroke="#fff" stroke-width="2"/></svg>
    <span class="offer-band__or">OR</span>
    <span class="offer-band__percent">10</span>
    <span class="offer-band__percent-sign">%</span>
    <span class="offer-band__per">PER<br>REFERRAL</span>
  </div>

  <div class="partner-ribbon">
    <span class="partner-ribbon__text partner-ribbon__premier">PREMIER</span>
    <span class="partner-ribbon__text partner-ribbon__program">PARTNER PROGRAM</span>
    <svg class="partner-ribbon__badge" viewBox="0 0 54 56">
      <path d="M27 3 L50 11 V27 C50 41 40 50 27 54 C14 50 4 41 4 27 V11 Z" fill="#fff"/>
      <path d="M27 9 L44 15 V27 C44 38 37 45 27 48 C17 45 10 38 10 27 V15 Z" fill="none" stroke="#c6202b" stroke-width="2"/>
      <path d="M17 28 L25 36 L39 18" fill="none" stroke="#1f3270" stroke-width="5" stroke-linecap="round" stroke-linejoin="round"/>
    </svg>
  </div>

  <h2 class="wins">PARTNER WITH US &amp; EVERYBODY WINS!</h2>

  <div class="benefits">
    <div class="benefit">
      <div class="benefit__title">GUARANTEED<br>PAYOUT</div>
      <div class="benefit__body">
        <svg class="benefit__icon" viewBox="0 0 30 30"><path d="M15 2 L26 6 V14 C26 21 21 26 15 28 C9 26 4 21 4 14 V6 Z" fill="#1e6fc0"/><path d="M9 15 L13 19 L21 10" fill="none" stroke="#fff" stroke-width="3" stroke-linecap="round" stroke-linejoin="round"/></svg>
        <p class="benefit__text">Minimum $500 or<br>10% of Total Invoice<br>Paid Fast</p>
      </div>
      <span class="benefit__dot"></span>
    </div>
    <div class="benefit">
      <div class="benefit__title">FREE<br>ESTIMATES</div>
      <div class="benefit__body">
        <svg class="benefit__icon" viewBox="0 0 30 30"><rect x="4" y="4" width="18" height="23" rx="2" fill="#1e6fc0"/><path d="M8 10h10M8 15h10M8 20h6" stroke="#fff" stroke-width="2"/><path d="M20 22 L27 9" stroke="#1f3270" stroke-width="3" stroke-linecap="round"/></svg>
        <p class="benefit__text">Fast &amp; Free<br>Inspections &amp;<br>Written Estimates</p>
      </div>
      <span class="benefit__dot"></span>
    </div>
    <div class="benefit">
      <div class="benefit__title">AFFORDABLE<br>SOLUTIONS</div>
      <div class="benefit__body">
        <svg class="benefit__icon" viewBox="0 0 30 30"><circle cx="17" cy="9" r="6" fill="#1e6fc0"/><path d="M2 22 H9 L14 19 H22 C24 19 24 22 22 22 H14 M2 27 H20 L28 20" fill="none" stroke="#1e6fc0" stroke-width="2.5" stroke-linecap="round" stroke-linejoin="round"/></svg>
        <p class="benefit__text">Lowest Out of Pocket;<br>Costs for Your<br>Customers</p>
      </div>
      <span class="benefit__dot"></span>
    </div>
    <div class="benefit">
      <div class="benefit__title">INDUSTRY<br>LEADERS</div>
      <div class="benefit__body">
        <svg class="benefit__icon" viewBox="0 0 30 30"><circle cx="15" cy="15" r="10" fill="none" stroke="#1e6fc0" stroke-width="5" stroke-dasharray="4 3"/><circle cx="15" cy="15" r="7" fill="#1e6fc0"/><path d="M15 10 L16.5 13.5 L20 14 L17.3 16.3 L18 20 L15 18 L12 20 L12.7 16.3 L10 14 L13.5 13.5 Z" fill="#fff"/></svg>
        <p class="benefit__text">Licensed &amp; Certified<br>Experts; Provide<br>100% Guarantee</p>
      </div>
      <span class="benefit__dot"></span>
    </div>
  </div>

  <p class="tagline">SEND <em>REFERRALS.</em> GET <em>PAID.</em> GROW <em>YOUR BUSINESS.</em></p>

  <div class="contact-bar">
    <div class="contact-bar__label">CALL, TEXT OR BOOK ONLINE</div>
    <div class="contact-bar__details">
      <span class="contact-bar__phone">858-472-6190</span>
      <span class="contact-bar__sep"></span>
      <span class="contact-bar__web">www.BrightKeelRebuilds.com</span>
    </div>
  </div>
</section>

<section class="flyer flyer--back" aria-label="Referral flyer back">
  <div class="back-hero"><div class="back-hero__shade"></div></div>
  <div class="back-photo" role="img" aria-label="Hundred-dollar bills with letter tiles spelling CASH FLOW"></div>
  <h2 class="back-headline">
    <span class="back-headline__lead">THE MORE YOU</span>
    <span class="back-headline__big">REFER</span>
    <span class="back-headline__lead">THE MORE YOU</span>
    <span class="back-headline__big">EARN</span>
  </h2>

  <div class="how-band">HOW IT WORKS</div>

  <div class="steps">
    <div class="step">
      <div class="step__photo step__photo--scan" role="img" aria-label="Thermal camera scanning an empty room for moisture"></div>
      <p class="step__label">REFER FLOOD, WATER<br>&amp; MOLD DAMAGE</p>
    </div>
    <div class="step">
      <div class="step__photo step__photo--inspect" role="img" aria-label="Inspector with clipboard outside a house"></div>
      <p class="step__label">WE TAKE CARE OF<br>EVERYTHING<span class="step__note">(evaluations/insurance)</span></p>
    </div>
    <div class="step">
      <div class="step__photo step__photo--sign" role="img" aria-label="Yellow road sign reading Get Paid to Share against a blue sky"></div>
      <p class="step__label">GET PAID TO<br>SHARE</p>
    </div>
  </div>

  <div class="contact-bar">
    <div class="contact-bar__label">CALL, TEXT OR BOOK ONLINE</div>
    <div class="contact-bar__details">
      <span class="contact-bar__phone">858-472-6190</span>
      <span class="contact-bar__sep"></span>
      <span class="contact-bar__web">www.BrightKeelRebuilds.com</span>
    </div>
  </div>
</section>

</body>
</html>
```